Vero M.Q. - Diagnostic Ultrasound Flyer

About US
Vero M.Q. is a concierge ultrasound company that provides onsite or offsite diagnostic ultrasounds. We have over 14 years experience in sonography, business management, and customer service. We offer both the physician and patient flexibility, convenience, and access to timely services.

We provide ultrasounds for the following specialties:
Obstetrics/Gynecology
Abdominal
Small Parts
Vascular

Company Features:
1. Onsite or Offsite Scans
2. Images Available Immediately for Referring Physician and Patient
3. Flexible Options for Ultrasound Interpretation/Billing
4. Access to Interpreting Radiologist
5. Final Report Process - 1-2 Business Days/ 1 hour for STAT.
6. PACS Storage with Secure Access.

We need a place to add in our contact information (address, email, website, phone)

We already have a logo and would like to use it ( they are attached). We would the colors to match the logo colors....maybe lighter version of yellow and blue.

```html
<!DOCTYPE html>
<html lang="en">
<head>
<meta charset="utf-8">
<title>Vero M.Q. – Diagnostic Ultrasound Flyer</title>
<link href="https://fonts.googleapis.com/css2?family=Montserrat:wght@500;600;700;800&display=swap" rel="stylesheet">
<style>
  :root{
    --backdrop:#e6e6e9;
    --white:#ffffff;
    --yellow:#fbbf2c;
    --blue:#3b3be3;
    --blue-text:#1f1fb4;
    --ink:#111111;
    --photo-warm:#d9a86a;
    --photo-light:#f1dcc0;
  }
  *{margin:0;padding:0;box-sizing:border-box}
  html,body{width:1200px;height:1200px;overflow:hidden;background:var(--backdrop)}
  body{font-family:"Montserrat",sans-serif;color:var(--ink)}
  .flyer{position:absolute;left:136px;top:0;width:928px;height:1200px;background:var(--yellow);overflow:hidden}
  .layer{position:absolute;left:0;top:0}
  .hero-photo{position:absolute;left:0;top:116px;width:928px;height:430px;
    background:linear-gradient(180deg,#7d6a5c 0%,var(--photo-warm) 45%,var(--photo-light) 72%,var(--yellow) 100%)}
  .side-photo{position:absolute;left:640px;top:560px;width:288px;height:380px;
    background:linear-gradient(90deg,rgba(251,191,44,0) 0%,#d7c3b2 45%,#b89a86 100%)}
  .header{position:absolute;left:0;top:0;width:928px;height:116px}
  .brand{position:absolute;left:55px;top:38px;display:flex;align-items:center;gap:12px}
  .brand-dot{width:22px;height:22px;border-radius:50%;background:var(--yellow)}
  .brand-name{font-weight:800;font-size:44px;letter-spacing:1px;color:var(--blue-text);line-height:1}
  .address{position:absolute;left:487px;top:36px;display:flex;align-items:center;gap:8px}
  .address p{font-size:18px;font-weight:500;line-height:26px}
  .intro{position:absolute;left:56px;top:540px;width:770px;font-size:17px;font-weight:500;line-height:26.5px}
  .specialties-title{position:absolute;left:56px;top:662px;font-size:23px;font-weight:700;color:var(--blue-text);white-space:nowrap}
  .specialties{position:absolute;left:56px;top:714px;width:560px;display:grid;grid-template-columns:222px 1fr;row-gap:14px;list-style:none}
  .specialties li{display:flex;align-items:center;gap:14px;font-size:25px;font-weight:500;color:var(--blue-text);line-height:32px;white-space:nowrap}
  .features-tab{position:absolute;left:31px;top:850px;width:278px;height:40px;background:var(--ink);
    border-radius:0 22px 22px 0;color:var(--white);font-weight:700;font-size:19px;padding-left:24px;line-height:40px;
    box-shadow:4px 0 0 var(--white)}
  .features{position:absolute;left:54px;top:911px;list-style:none;color:var(--white);font-weight:700;font-size:15.5px;width:540px}
  .features li{display:flex;gap:6px;line-height:22px;margin-bottom:8px}
  .features .num{color:var(--yellow)}
  .circle{position:absolute;border-radius:50%;border:3px solid var(--white)}
  .circle-prints{left:484px;top:792px;width:202px;height:202px;background:radial-gradient(circle,#a0524a 0%,#4a3a3a 45%,#d9d9d9 75%)}
  .circle-hands{left:612px;top:818px;width:284px;height:284px;background:radial-gradient(circle at 65% 40%,#d9874f 0%,#6f5a52 40%,#cfc8c4 80%)}
  .contact-bar{position:absolute;left:0;top:1131px;width:928px;height:69px;background:var(--yellow);
    display:flex;align-items:center;justify-content:center;gap:12px;font-weight:700;font-size:26px}
  .contact-item{display:flex;align-items:center;gap:8px}
  .sep{font-weight:500}
</style>
</head>
<body>
<div class="flyer">
  <div class="hero-photo" role="img" aria-label="Photo: expectant mother smiling at her partner during an ultrasound, with a 3D scan on the monitor"></div>
  <div class="side-photo" role="img" aria-label="Photo: sonographer operating an ultrasound console beside a patient"></div>

  <svg class="layer" width="928" height="1200" viewBox="0 0 928 1200" aria-hidden="true">
    <polygon points="0,0 928,0 928,128 430,160 0,118" fill="var(--white)"/>
    <polygon points="0,118 430,160 680,205 640,222 0,128" fill="var(--yellow)"/>
    <polygon points="430,160 928,128 928,205 680,205" fill="var(--blue)"/>
    <polygon points="0,858 928,940 928,1131 0,1131" fill="var(--blue)"/>
    <polygon points="0,850 928,916 928,940 0,860" fill="var(--ink)"/>
  </svg>

  <header class="header">
    <div class="brand">
      <span class="brand-name">VERO M.Q.</span>
      <span class="brand-dot"></span>
    </div>
    <div class="address">
      <svg width="28" height="38" viewBox="0 0 24 32" aria-hidden="true"><path d="M12 0C5.4 0 0 5.3 0 11.8 0 20.6 12 32 12 32s12-11.4 12-20.2C24 5.3 18.6 0 12 0zm0 16.5a4.7 4.7 0 1 1 0-9.4 4.7 4.7 0 0 1 0 9.4z" fill="var(--ink)"/></svg>
      <p>4180 Harbor Point Road Suite B2<br>Fairmont, MD 20600 USA</p>
    </div>
  </header>

  <p class="intro">Vero M.Q. is a concierge ultrasound company that provides onsite or offsite diagnostic ultrasounds. We have over 14 years experience in sonography, business management, and customer service. We offer both the physician and patient flexibility, convenience, and access to timely services.</p>

  <h2 class="specialties-title">We provide ultrasounds for the following specialties:</h2>
  <ul class="specialties">
    <li><svg width="24" height="24" viewBox="0 0 24 24" aria-hidden="true"><path d="M2 13l6 7L22 3" stroke="var(--blue-text)" stroke-width="4" fill="none"/></svg>Small Parts</li>
    <li><svg width="24" height="24" viewBox="0 0 24 24" aria-hidden="true"><path d="M2 13l6 7L22 3" stroke="var(--blue-text)" stroke-width="4" fill="none"/></svg>Obstetrics/Gynecology</li>
    <li><svg width="24" height="24" viewBox="0 0 24 24" aria-hidden="true"><path d="M2 13l6 7L22 3" stroke="var(--blue-text)" stroke-width="4" fill="none"/></svg>Abdominal</li>
    <li><svg width="24" height="24" viewBox="0 0 24 24" aria-hidden="true"><path d="M2 13l6 7L22 3" stroke="var(--blue-text)" stroke-width="4" fill="none"/></svg>Vascular</li>
  </ul>

  <div class="features-tab">Company Features:</div>
  <ol class="features">
    <li><span class="num">1.</span><span>Onsite or Offsite Scans</span></li>
    <li><span class="num">2.</span><span>Images Available Immediately for Referring<br>Physician and Patient</span></li>
    <li><span class="num">3.</span><span>Flexible Options for Ultrasound Interpretation/Billing</span></li>
    <li><span class="num">4.</span><span>Access to Interpreting Radiologist</span></li>
    <li><span class="num">5.</span><span>Final Report Process - 1-2 Business Days/ 1 hour for STAT.</span></li>
    <li><span class="num">6.</span><span>PACS Storage with Secure Access.</span></li>
  </ol>

  <div class="circle circle-hands" role="img" aria-label="Photo: hands holding a printed 3D ultrasound image"></div>
  <div class="circle circle-prints" role="img" aria-label="Photo: printed ultrasound scans lying on a knit blanket"></div>

  <footer class="contact-bar">
    <span class="contact-item"><svg width="20" height="20" viewBox="0 0 24 24" aria-hidden="true"><path d="M6.6 10.8a15 15 0 0 0 6.6 6.6l2.2-2.2c.3-.3.7-.4 1-.2 1.1.4 2.3.6 3.6.6.6 0 1 .4 1 1V20c0 .6-.4 1-1 1A17 17 0 0 1 3 4c0-.6.4-1 1-1h3.5c.6 0 1 .4 1 1 0 1.3.2 2.5.6 3.6.1.3 0 .7-.2 1z" fill="var(--ink)"/></svg>(301) 555-0148</span>
    <span class="sep">|</span>
    <span class="contact-item"><svg width="20" height="20" viewBox="0 0 24 24" aria-hidden="true" fill="none" stroke="var(--ink)" stroke-width="2.2"><circle cx="12" cy="12" r="10"/><ellipse cx="12" cy="12" rx="4.5" ry="10"/><path d="M2 12h20"/></svg>www.vero-mq.com</span>
    <span class="sep">|</span>
    <span class="contact-item"><svg width="24" height="18" viewBox="0 0 24 18" aria-hidden="true"><rect x="1" y="1" width="22" height="16" fill="none" stroke="var(--ink)" stroke-width="2.2"/><path d="M1 1l11 9 11-9" fill="none" stroke="var(--ink)" stroke-width="2.2"/></svg>info@vero-mq.com</span>
  </footer>
</div>
</body>
</html>
```